Morvex Business Card (intended for Business Card sized magnet)

Hi guys,

I would like to get a design for my business card for the restaurant. The design must be single sided as I intend to produce business card sized magnets.

The File attached must me on and I'm open for new ides

Can you please ensure that the design meets Cardowell's magnetic business card size specifications:

http://www.cardowell.example.au/custom-magnets.aspx?txi=15695&xnid=TopNav_Magnetic+Business+Cards+(linked+item)_Magnets_Marketing+Products&xnav=TopNav

Full Bleed Size (starting document size):
90 x 52 mm
1062 x 615 pixels
* Finished artwork should use the full bleed dimensions for best results.

Document Trim Size (final size after being cut):
87 x 49 mm
1028 x 579 pixels
* Please be sure to keep all text within the safe margin.

Resolution:
300 DPI

The winning design/source files need to meet these specifications.

Thanks
Updates

Hi guys, can I see more options please Thanks

```html
<!DOCTYPE html>
<html lang="en">
<head>
<meta charset="utf-8">
<title>Morvex Business Card</title>
<link href="https://fonts.googleapis.com/css2?family=Cardo&family=Alegreya+Sans+SC&display=swap" rel="stylesheet">
<style>
  :root {
    --paper: #ffffff;
    --ink: #111111;
    --rule: #1a1a1a;
    --band-light: #ecebe8;
    --band-mid: #d6d4cf;
  }
  html, body {
    margin: 0;
    padding: 0;
    overflow: hidden;
    background: var(--paper);
  }
  .card {
    position: relative;
    width: 1200px;
    height: 686px;
    background: var(--paper);
    overflow: hidden;
  }
  .border-band {
    position: absolute;
    left: 0;
    width: 1200px;
    height: 57px;
    border-top: 3px solid var(--rule);
    border-bottom: 2px solid var(--rule);
    background: linear-gradient(90deg, var(--band-light), var(--band-mid) 50%, var(--band-light));
    box-sizing: border-box;
  }
  .border-band--top { top: 55px; }
  .border-band--bottom { top: 593px; }

  .brand {
    position: absolute;
    left: 75px;
    top: 0;
    width: 353px;
  }
  .brand-name {
    position: absolute;
    left: 0;
    top: 242px;
    width: 353px;
    margin: 0;
    text-align: center;
    font-family: "Cardo", serif;
    font-weight: 400;
    font-size: 106px;
    line-height: 1;
    color: var(--ink);
    white-space: nowrap;
  }
  .brand-ornament {
    position: absolute;
    left: 0;
    top: 352px;
    width: 353px;
    height: 120px;
    border-top: 4px solid var(--rule);
    border-bottom: 4px solid var(--rule);
    box-sizing: border-box;
    background: linear-gradient(90deg, var(--band-light), var(--band-mid) 50%, var(--band-light));
  }
  .divider {
    position: absolute;
    left: 484px;
    top: 235px;
    width: 3px;
    height: 243px;
    background: var(--rule);
  }
  .contact {
    position: absolute;
    left: 543px;
    top: 232px;
    margin: 0;
    padding: 0;
    list-style: none;
    font-family: "Alegreya Sans SC", sans-serif;
    font-size: 31px;
    color: var(--ink);
  }
  .contact li {
    height: 66.5px;
    line-height: 40px;
    white-space: nowrap;
  }
</style>
</head>
<body>
  <main class="card">
    <div class="border-band border-band--top" role="img" aria-label="Decorative geometric star pattern border"></div>

    <div class="brand">
      <h1 class="brand-name">Morvex</h1>
      <div class="brand-ornament" role="img" aria-label="Geometric star ornament with red, teal and yellow centres"></div>
    </div>

    <div class="divider"></div>

    <ul class="contact">
      <li class="contact__address">214 Orrin Vale rd, ashbury north, 3187</li>
      <li class="contact__phone">03 9418 2073</li>
      <li class="contact__web">www.morvex.com.au</li>
      <li class="contact__email">Morvex214@mailpost.com</li>
    </ul>

    <div class="border-band border-band--bottom" role="img" aria-label="Decorative geometric star pattern border"></div>
  </main>
</body>
</html>
```